Rebrand/migrate of website to Wordpress

Rebrand/transfer of php website to new wordpress website using the Noxel theme. Dial4LessLines.com is being rebranded to Quorvix and therefore we are looking to simplify the current layout to match competitors sites and be mobile device friendly.
The new site will need to show services in a clear uncluttered way with more emphasis on the service rather than large amounts of text. See attachment B1 for example.
Competitors sites are kx.com , ringmoor.co.uk, zelwire.com
Updates

As I have had a few request from designers to extend the deadline. I have requested Pixel Harbor to extend to Tuesday 3rd April 2018

Target Market(s)

UK Home phone and small business customers

Industry/Entity Type

Telecom

Coding

Coded - Design and coding required

Number of Pages Required

5+ page

Colors

Designer to choose colors to be used in the design.

Requirements
Must have
• 1. Use Noxel wordpress theme that will be supplied.
• 2. Combine the best layouts where possible as used by competitors but in a unique way.
• 3. Horizontal bar should be in white so that it can layer over banner as per file A1.
• 4. Simplify current layout to match competitors see attached file B1.
• 5. Integrate Tallbranch - Tallbranch Leads Web / web form to capture interested customers - name, Company name, Telephone number, email address.
Should not have
• Colour scheme that is the same as our competitors RingMoor, KX, Halden, Vexa Net

```html
<!DOCTYPE html>
<html lang="en">
<head>
<meta charset="utf-8">
<title>Quorvix – Switch To Cheaper Calls</title>
<link rel="stylesheet" href="https://fonts.googleapis.com/css2?family=Poppins:wght@400;500;600&family=Roboto+Condensed:wght@300;400;700&family=Roboto:wght@700;900&display=swap">
<style>
:root{
  --cyan:#00aeea;
  --cyan-soft:#8fdcf5;
  --orange:#f7931e;
  --magenta:#d2127a;
  --magenta-soft:#ecb3d3;
  --ink:#2b2b2b;
  --grey:#6f6f6f;
  --topbar:#585858;
  --footer-dark:#242424;
  --white:#ffffff;
  --gold:#f2b705;
}
*{box-sizing:border-box;margin:0;padding:0}
html,body{width:1200px;height:3536px;overflow:hidden}
body{position:relative;background:var(--white);font-family:"Poppins",sans-serif;color:var(--ink)}
.abs{position:absolute}

/* top bar */
.topbar{top:0;left:0;width:1200px;height:35px;background:var(--topbar);color:var(--white);font-size:12px;font-weight:600;letter-spacing:.3px}
.topbar .order{left:113px;top:10px}
.topbar .order b{font-size:14px;margin-left:6px}
.topbar .account{right:100px;top:7px;height:22px;padding:0 10px 0 26px;line-height:22px;font-size:10px;background:#444;border-radius:2px}
.topbar .account svg{position:absolute;left:9px;top:5px}

/* nav */
.nav{top:35px;left:0;width:1200px;height:78px;background:var(--white)}
.brand{font-family:"Poppins",sans-serif;font-weight:500;color:var(--orange);font-size:38px;letter-spacing:-.5px}
.nav .brand{left:113px;top:12px}
.nav ul{list-style:none;left:540px;top:29px;display:flex;gap:0}
.nav li{font-size:14px;color:#333;margin-right:52px}
.nav li.active{color:var(--orange)}

/* hero */
.hero-photo{top:113px;left:0;width:1200px;height:600px;
  background:radial-gradient(ellipse at 75% 35%,#e9c6a8 0%,#b98660 25%,transparent 55%),
             linear-gradient(90deg,#4b3a31 0%,#7a5f4c 35%,#a57a58 60%,#6b4a36 100%)}
.hero h1{left:113px;top:220px;font-family:"Roboto",sans-serif;font-weight:900;color:var(--cyan);font-size:60px;line-height:68px;letter-spacing:1px}
.hero p{left:113px;top:380px;width:540px;color:var(--white);font-size:17px;font-weight:500;line-height:34px}
.btn{display:block;text-align:center;border-radius:30px;font-size:12px;font-weight:600;text-transform:uppercase;letter-spacing:.3px}
.btn-solid{background:var(--orange);color:var(--white)}
.btn-line{border:2px solid currentColor;background:transparent}
.hero .btn{left:113px;top:514px;width:146px;height:46px;line-height:46px}

/* get started */
.start-band{top:700px;left:0;width:1200px;height:540px;background:var(--cyan)}
.section-title{width:1200px;left:0;text-align:center;font-family:"Roboto Condensed",sans-serif;font-weight:300;font-size:40px}
.section-title b{font-weight:700}
.section-lead{left:240px;width:720px;text-align:center;font-size:12px;line-height:24px}
.start .section-title{top:775px;color:var(--white)}
.start .section-lead{top:830px;color:var(--white)}
.plan-card{top:924px;width:395px;height:214px;background:var(--white);box-shadow:0 6px 18px rgba(0,0,0,.18)}
.plan-card .badge{left:-34px;top:56px;width:100px;height:100px;border-radius:50%;background:#efefef}
.plan-card .badge svg{position:absolute;left:35px;top:34px}
.plan-card h3{left:100px;top:30px;font-family:"Roboto Condensed",sans-serif;font-weight:700;font-size:24px}
.plan-card p{left:100px;top:66px;width:260px;font-size:12px;line-height:24px;color:var(--grey)}
.plan-card .btn{left:100px;top:132px;width:158px;height:42px;line-height:38px;font-size:11px}
.plan-business{left:189px}
.plan-business h3,.plan-business .btn{color:var(--orange)}
.plan-home{left:653px}
.plan-home h3,.plan-home .btn{color:var(--cyan)}

/* features */
.features .section-title{top:1378px;color:#222}
.features .section-lead{top:1440px;color:var(--grey)}
.feature{width:300px;height:130px}
.feature .dot{left:0;top:0;width:44px;height:44px;border-radius:50%}
.feature .dot svg{position:absolute;left:12px;top:12px}
.feature h4{left:62px;top:6px;font-size:14px;font-weight:500;color:#222}
.feature p{left:62px;top:32px;width:235px;font-size:12px;line-height:24px;color:var(--grey)}
.features .btn{left:521px;top:1855px;width:158px;height:42px;line-height:38px;color:var(--orange);font-size:11px}

/* refer band */
.refer-band{top:1980px;left:0;width:1200px;height:372px;
  background:linear-gradient(90deg,var(--orange) 0%,var(--orange) 50%,#e6a255 58%,#b07a52 70%,#7d4f3c 100%)}
.refer .line{left:113px;font-family:"Roboto Condensed",sans-serif;color:var(--white);font-size:44px;font-weight:400;letter-spacing:.5px}
.refer .big{color:var(--magenta);font-weight:700;font-size:52px}
.refer .btn{left:113px;top:2244px;width:150px;height:48px;line-height:44px;color:var(--white)}

/* reviews */
.reviews .section-title{top:2440px;color:#222}
.reviews .section-lead{top:2495px;color:var(--grey)}
.review{background:var(--white);box-shadow:0 2px 14px rgba(0,0,0,.12)}
.review .stars{left:20px;top:26px;display:flex;gap:2px}
.review .date{right:20px;top:27px;font-size:12px;color:#444}
.review p{left:30px;width:calc(100% - 60px);top:78px;text-align:center;font-size:12px;line-height:24px;color:var(--grey)}
.review .who{left:0;width:100%;top:150px;text-align:center;font-size:12px;font-weight:500;color:var(--orange)}
.review-featured{box-shadow:0 10px 26px rgba(0,0,0,.18)}
.pager{top:2852px;left:566px;display:flex;gap:10px}
.pager span{width:9px;height:9px;border-radius:50%}

/* footer */
.footer-band{top:3020px;left:0;width:1200px;height:400px;background:var(--magenta)}
.footer .brand{left:175px;top:3100px;font-size:38px}
.footer .about{left:115px;top:3160px;width:350px;text-align:center;color:var(--white);font-size:11px;line-height:23px}
.footer .vrule{top:3090px;width:1px;height:220px;background:rgba(255,255,255,.3)}
.footer h5{font-size:17px;font-weight:400;color:var(--white)}
.footer ul{list-style:none;color:var(--white);font-size:11px;line-height:22px}
.footer .notes{left:679px;top:3140px;width:405px;color:var(--white);font-size:11px;line-height:23px}
.bottom-bar{top:3441px;left:0;width:1200px;height:95px;background:var(--footer-dark)}
.social{top:3472px;width:38px;height:38px;border-radius:50%;background:var(--white)}
.search{top:3474px;left:490px;width:220px;height:36px;border-radius:18px;background:var(--white)}
.search .go{right:0;top:0;width:56px;height:36px;border-radius:18px;background:var(--magenta);color:var(--white);font-size:12px;font-weight:600;text-align:center;line-height:36px}
.copy{top:3484px;right:113px;color:#cfcfcf;font-size:11px}
</style>
</head>
<body>

<!-- top bar -->
<div class="abs topbar">
  <div class="abs order">ORDER BY FREE PHONE : <b>0800 417 2290</b></div>
  <div class="abs account">
    <svg width="11" height="12" viewBox="0 0 11 12"><circle cx="5.5" cy="3.2" r="3" fill="#fff"/><path d="M0 12c0-3.5 2.5-5 5.5-5s5.5 1.5 5.5 5z" fill="#fff"/></svg>
    MY ACCOUNT
  </div>
</div>

<!-- navigation -->
<header class="abs nav">
  <div class="abs brand">quorvix</div>
  <ul class="abs">
    <li class="active">Home</li><li>About Us</li><li>Business</li><li>Residential</li><li>Support</li><li>Contact</li>
  </ul>
</header>

<!-- hero -->
<section class="hero">
  <div class="abs hero-photo" role="img" aria-label="Smiling woman in glasses talking on a mobile phone in a softly blurred café"></div>
  <h1 class="abs">Switch To<br>Cheaper Calls Now !</h1>
  <p class="abs">Make Cheap LOCAL, NATIONAL &amp; INTERNATIONAL Unlimited Phone Calls To Your Friends, Family And More With Our Great Calling Plans.</p>
  <a class="abs btn btn-solid">Start Here</a>
</section>

<!-- waves into cyan band -->
<svg class="abs" style="top:600px;left:0" width="1200" height="110" viewBox="0 0 1200 110" preserveAspectRatio="none">
  <path d="M0 40 C220 10 420 20 620 40 C820 60 1000 70 1200 60 L1200 110 L0 110 Z" fill="var(--cyan)"/>
</svg>
<div class="abs start-band"></div>
<svg class="abs" style="top:1200px;left:0" width="1200" height="120" viewBox="0 0 1200 120" preserveAspectRatio="none">
  <path d="M0 50 C250 10 450 100 700 70 C900 45 1050 10 1200 30 L1200 120 C1000 80 800 60 600 90 C400 120 200 80 0 100 Z" fill="var(--cyan-soft)"/>
  <path d="M0 0 L1200 0 L1200 20 C1050 20 900 70 650 90 C420 110 250 40 0 70 Z" fill="var(--cyan)"/>
</svg>

<section class="start">
  <h2 class="abs section-title">Ready to <b>Get Started</b></h2>
  <p class="abs section-lead">Lorem ipsum dolor sit amet, consectetuer adipiscing elit, sed diam nonummy nibh euismod tincidunt ut laoreet dolore magna aliquam erat volutpat. Ut wisi enim ad minim veniam, quis ullamcorper suscipit lobortis.</p>

  <article class="abs plan-card plan-business">
    <div class="abs badge">
      <svg width="32" height="30" viewBox="0 0 32 30"><rect x="10" y="1" width="12" height="6" rx="2" fill="none" stroke="var(--orange)" stroke-width="3"/><rect x="1" y="7" width="30" height="21" rx="3" fill="var(--orange)"/><rect x="13" y="14" width="6" height="5" fill="#efefef"/></svg>
    </div>
    <h3 class="abs">FOR BUSINESS</h3>
    <p class="abs">Lorem ipsum dolor sit amet, consectetuer adipiscing elit, sed dia.</p>
    <a class="abs btn btn-line">Get Started Now</a>
  </article>

  <article class="abs plan-card plan-home">
    <div class="abs badge">
      <svg width="32" height="30" viewBox="0 0 32 30"><path d="M16 1 L31 12 L1 12 Z" fill="var(--cyan)"/><rect x="4" y="12" width="24" height="17" fill="var(--cyan)"/><rect x="8" y="16" width="4" height="4" fill="#efefef"/><rect x="20" y="16" width="4" height="4" fill="#efefef"/><rect x="14" y="20" width="4" height="9" fill="#efefef"/></svg>
    </div>
    <h3 class="abs">FOR RESIDENTIAL</h3>
    <p class="abs">Lorem ipsum dolor sit amet, consectetuer adipiscing elit, sed dia.</p>
    <a class="abs btn btn-line">Get Started Now</a>
  </article>
</section>

<!-- features -->
<section class="features">
  <h2 class="abs section-title">Quorvix <b>Feautres &amp; Benefits</b></h2>
  <p class="abs section-lead">Lorem ipsum dolor sit amet, consectetuer adipiscing elit, sed diam nonummy nibh euismod tincidunt ut laoreet dolore magna aliquam erat volutpat. Ut wisi enim ad minim veniam, quis ullamcorper suscipit lobortis.</p>

  <div class="abs feature" style="left:113px;top:1526px">
    <div class="abs dot" style="background:var(--cyan)"><svg width="20" height="20" viewBox="0 0 20 20"><rect x="2" y="4" width="16" height="12" rx="1" fill="none" stroke="#fff" stroke-width="2"/><path d="M2 5 L10 11 L18 5" fill="none" stroke="#fff" stroke-width="2"/></svg></div>
    <h4 class="abs">FEAUTRES &amp; BENEFITS ONE</h4>
    <p class="abs">Lorem ipsum dolor sit met, consectetuer adipiscing elit, sed diam nonummy nibh euismod tincidunt aoreet dolore magna aliquam erat volutpat.</p>
  </div>
  <div class="abs feature" style="left:450px;top:1526px">
    <div class="abs dot" style="background:var(--orange)"><svg width="20" height="20" viewBox="0 0 20 20"><path d="M5 2 L8 6 L6 8 C7 11 9 13 12 14 L14 12 L18 15 L16 18 C9 18 2 11 2 4 Z" fill="#fff"/></svg></div>
    <h4 class="abs">FEAUTRES &amp; BENEFITS ONE</h4>
    <p class="abs">Lorem ipsum dolor sit met, consectetuer adipiscing elit, sed diam nonummy nibh euismod tincidunt aoreet dolore magna aliquam erat volutpat.</p>
  </div>
  <div class="abs feature" style="left:787px;top:1526px">
    <div class="abs dot" style="background:var(--magenta)"><svg width="20" height="20" viewBox="0 0 20 20"><circle cx="10" cy="8" r="6" fill="none" stroke="#fff" stroke-width="2"/><rect x="7" y="14" width="6" height="4" fill="#fff"/></svg></div>
    <h4 class="abs">FEAUTRES &amp; BENEFITS ONE</h4>
    <p class="abs">Lorem ipsum dolor sit met, consectetuer adipiscing elit, sed diam nonummy nibh euismod tincidunt aoreet dolore magna aliquam erat volutpat.</p>
  </div>
  <div class="abs feature" style="left:113px;top:1689px">
    <div class="abs dot" style="background:var(--magenta)"><svg width="20" height="20" viewBox="0 0 20 20"><path d="M2 3 H18 V14 H8 L4 18 V14 H2 Z" fill="none" stroke="#fff" stroke-width="2"/></svg></div>
    <h4 class="abs">FEAUTRES &amp; BENEFITS ONE</h4>
    <p class="abs">Lorem ipsum dolor sit met, consectetuer adipiscing elit, sed diam nonummy nibh euismod tincidunt aoreet dolore magna aliquam erat volutpat.</p>
  </div>
  <div class="abs feature" style="left:450px;top:1689px">
    <div class="abs dot" style="background:#7cc242"><svg width="20" height="20" viewBox="0 0 20 20"><path d="M3 10 L8 15 L17 5" fill="none" stroke="#fff" stroke-width="2.5"/></svg></div>
    <h4 class="abs">FEAUTRES &amp; BENEFITS ONE</h4>
    <p class="abs">Lorem ipsum dolor sit met, consectetuer adipiscing elit, sed diam nonummy nibh euismod tincidunt aoreet dolore magna aliquam erat volutpat.</p>
  </div>
  <div class="abs feature" style="left:787px;top:1689px">
    <div class="abs dot" style="background:#f7a23c"><svg width="20" height="20" viewBox="0 0 20 20"><circle cx="10" cy="10" r="7" fill="none" stroke="#fff" stroke-width="2"/><path d="M10 6 V10 L13 12" fill="none" stroke="#fff" stroke-width="2"/></svg></div>
    <h4 class="abs">FEAUTRES &amp; BENEFITS ONE</h4>
    <p class="abs">Lorem ipsum dolor sit met, consectetuer adipiscing elit, sed diam nonummy nibh euismod tincidunt aoreet dolore magna aliquam erat volutpat.</p>
  </div>

  <a class="abs btn btn-line">View All Feautres</a>
</section>

<!-- refer a friend -->
<section class="refer">
  <div class="abs refer-band" role="img" aria-label="Two smiling young women looking at a phone together, photo fading into orange"></div>
  <div class="abs line" style="top:2030px">REFER A FRIEND AND</div>
  <div class="abs line" style="top:2092px">GET 2 MONTHS</div>
  <div class="abs line big" style="top:2152px">FREE CALL PACKAGE</div>
  <a class="abs btn btn-line">Start Here</a>
</section>

<!-- reviews -->
<section class="reviews">
  <h2 class="abs section-title">Customer <b>Review</b></h2>
  <p class="abs section-lead">Lorem ipsum dolor sit amet, consectetuer adipiscing elit, sed diam nonummy nibh euismod tincidunt ut laoreet dolore magna aliquam erat volutpat. Ut wisi enim ad minim veniam, quis nostrud exerci tation ullamcorper suscipit lobortis.</p>

  <article class="abs review" style="left:113px;top:2595px;width:305px;height:190px">
    <div class="abs stars"><svg width="84" height="14" viewBox="0 0 84 14"><g fill="var(--gold)"><path id="st" d="M7 0 L9 5 L14 5 L10 8 L11.5 13.5 L7 10 L2.5 13.5 L4 8 L0 5 L5 5 Z"/><use href="#st" x="17"/><use href="#st" x="34"/><use href="#st" x="51"/><use href="#st" x="68"/></g></svg></div>
    <div class="abs date">26.03.2018</div>
    <p class="abs">I'm more likely to just pick up the phone... Instead of using email I now speak to people just pick up the phone...</p>
    <div class="abs who">Harriet K, Leeds</div>
  </article>
  <article class="abs review review-featured" style="left:446px;top:2598px;width:306px;height:208px">
    <div class="abs stars"><svg width="84" height="14" viewBox="0 0 84 14"><g fill="var(--gold)"><use href="#st"/><use href="#st" x="17"/><use href="#st" x="34"/><use href="#st" x="51"/><use href="#st" x="68"/></g></svg></div>
    <div class="abs date">26.03.2018</div>
    <p class="abs">I'm more likely to just pick up the phone... Instead of using email I now speak to people just pick up the phone...</p>
    <div class="abs who" style="top:160px">Harriet K, Leeds</div>
  </article>
  <article class="abs review" style="left:781px;top:2595px;width:306px;height:190px">
    <div class="abs stars"><svg width="84" height="14" viewBox="0 0 84 14"><g fill="var(--gold)"><use href="#st"/><use href="#st" x="17"/><use href="#st" x="34"/><use href="#st" x="51"/><use href="#st" x="68"/></g></svg></div>
    <div class="abs date">26.03.2018</div>
    <p class="abs">I'm more likely to just pick up the phone... Instead of using email I now speak to people just pick up the phone...</p>
    <div class="abs who">Harriet K, Leeds</div>
  </article>

  <div class="abs pager">
    <span style="background:var(--magenta)"></span><span style="background:var(--cyan)"></span><span style="background:var(--orange)"></span><span style="background:#3d5a6b"></span>
  </div>
</section>

<!-- footer -->
<footer class="footer">
  <svg class="abs" style="top:2930px;left:0" width="1200" height="100" viewBox="0 0 1200 100" preserveAspectRatio="none">
    <path d="M0 40 C180 0 360 10 520 35 C700 65 880 20 1050 15 C1120 13 1170 25 1200 35 L1200 100 L0 100 Z" fill="var(--magenta-soft)"/>
    <path d="M0 80 C200 60 400 20 600 30 C800 40 1000 70 1200 60 L1200 100 L0 100 Z" fill="var(--magenta)"/>
  </svg>
  <div class="abs footer-band"></div>

  <div class="abs brand">quorvix</div>
  <p class="abs about">Lorem ipsum dolor sit amet, consectetuer adipiscing elit, sed diam nonummy nibh euismod tincidunt ut laoreet dolore magna aliquam erat volutpat. nibh euismod tincidunt</p>

  <div class="abs vrule" style="left:463px"></div>
  <div class="abs vrule" style="left:637px"></div>

  <h5 class="abs" style="left:497px;top:3096px">Company</h5>
  <ul class="abs" style="left:497px;top:3130px">
    <li>Home</li><li>About Us</li><li>Business</li><li>Residential</li><li>Support</li><li>Contact</li>
  </ul>

  <h5 class="abs" style="left:679px;top:3096px">Notes For You</h5>
  <p class="abs notes">(Applies to UK landline numbers starting with 01, 02 and 03. International landlines calls to countries in our call plans are unlimited and do not include calls to mobiles unless specified.<br>Calls are billed on a per second increment. Fair usage policy applies.</p>

  <svg class="abs" style="top:3370px;left:0" width="1200" height="72" viewBox="0 0 1200 72" preserveAspectRatio="none">
    <path d="M0 50 C200 70 420 20 640 15 C860 10 1040 40 1200 30 L1200 72 L0 72 Z" fill="var(--footer-dark)"/>
  </svg>
  <div class="abs bottom-bar"></div>
  <div class="abs social" style="left:113px" role="img" aria-label="Social network link"></div>
  <div class="abs social" style="left:161px" role="img" aria-label="Social network link"></div>
  <div class="abs search"><div class="abs go">GO</div></div>
  <div class="abs copy">© All Rights Reserved 2018.</div>
</footer>

</body>
</html>
```